Profile Card Layout/Design Template

We recently ran a workshop with a client and during that workshop we developed some typical profiles of their target audience using flip chart paper. We now want to turn the profiles into professionally designed A5 cards we can then print and give to the client, therefore we require the profile card layout template to be designed so that in the future we can insert the profile data and images in-house.
Attached are 3 files.
1. persona_sallysocial.jpg is one of profiles we want to convert
2. profilecards.png is an example of the type of design/layout we need to convert the flip chart data to.
3. our company logo
So the layout needs to provide space for
- the profile data specified in persona_sallysocial.jpg
- some additional space for a profile summary/overview not currently shown in persona_sallysocial.jpg but
- an image/photo of the profiled person
- a placeholder for the clients logo
- a placeholder for our company logo
- placeholders for appropriate images to compliment the profile
Happy to consider both portrait and landscape designs
Would be good but not essential if we could change colours of specific elements of the design to compliment the clients corporate colours. So for instance our current clients corporate colours are #b50700, #001739 & #000000

```html
<!DOCTYPE html>
<html lang="en">
<head>
<meta charset="utf-8">
<title>Sally Social – Profile Card</title>
<link href="https://fonts.googleapis.com/css2?family=Montserrat:wght@500;700&family=Open+Sans:wght@400;600&family=Architects+Daughter&display=swap" rel="stylesheet">
<style>
  :root {
    --card-bg: #ffffff;
    --page-bg: #ffffff;
    --frame: #6b1017;
    --panel: #f990c8;
    --ink: #1a1a1a;
    --muted-line: #555555;
    --photo-top: #c9b9b4;
    --photo-bottom: #c8333f;
    --clip: #9a9a9a;
    --accent: #3c8f2e;
  }
  * { box-sizing: border-box; margin: 0; padding: 0; }
  html, body {
    width: 1200px; height: 848px; overflow: hidden;
    background: var(--page-bg);
  }
  .profile-card {
    position: relative; width: 1200px; height: 848px;
    font-family: "Open Sans", Arial, sans-serif; color: var(--ink);
  }
  .card-frame {
    position: absolute; left: 56px; top: 52px; width: 1092px; height: 744px;
    border: 4px solid var(--frame); border-radius: 24px; background: var(--card-bg);
  }
  .persona-name {
    position: absolute; left: 366px; top: 80px; width: 390px; text-align: center;
    font-family: "Montserrat", Arial, sans-serif; font-weight: 500;
    font-size: 50px; letter-spacing: 1px; line-height: 1;
  }
  .section-title {
    position: absolute;
    font-family: "Montserrat", Arial, sans-serif; font-weight: 700;
    font-size: 17px; text-transform: uppercase; line-height: 1;
    padding-bottom: 5px; border-bottom: 1.5px solid var(--ink);
  }
  .panel {
    position: absolute; background: var(--panel); border-radius: 16px;
  }
  .trait-list {
    list-style: none; padding: 18px 16px;
    font-size: 13.5px; line-height: 22px;
  }
  .trait-list li { position: relative; padding-left: 22px; }
  .trait-list li::before {
    content: ""; position: absolute; left: 2px; top: 7px;
    width: 9px; height: 9px; border-radius: 50%; background: var(--ink);
  }
  .motivations-title { left: 90px; top: 76px; }
  .motivations { left: 76px; top: 116px; width: 264px; height: 154px; }
  .behaviour-title { left: 92px; top: 342px; }
  .behaviour { left: 76px; top: 376px; width: 264px; height: 140px; }
  .frustrations-title { left: 90px; top: 576px; }
  .frustrations { left: 76px; top: 612px; width: 264px; height: 154px; }
  .pain-title { left: 400px; top: 582px; }
  .pain-points { left: 386px; top: 614px; width: 270px; height: 152px; }
  .pain-points .trait-list, .frustrations .trait-list { padding-top: 14px; }

  .portrait-panel { left: 366px; top: 166px; width: 364px; height: 370px; }
  .photo-frame {
    position: absolute; left: 504px; top: 152px; width: 222px; height: 290px;
    background: #fff; transform: rotate(3deg);
    box-shadow: 2px 3px 6px rgba(0,0,0,0.35);
  }
  .photo-placeholder {
    position: absolute; left: 14px; top: 14px; width: 194px; height: 244px;
    background: linear-gradient(180deg, var(--photo-top) 0%, #d8cbc6 45%, var(--photo-bottom) 80%);
  }
  .paper-clip {
    position: absolute; left: 640px; top: 118px; width: 30px; height: 70px;
    border: 4px solid var(--clip); border-radius: 15px; transform: rotate(-22deg);
  }
  .persona-goal {
    position: absolute; left: 376px; top: 456px; width: 360px;
    font-family: "Architects Daughter", cursive; font-size: 19px; line-height: 24px;
  }

  .summary-title { left: 770px; top: 64px; }
  .summary { left: 756px; top: 110px; width: 374px; height: 270px; }
  .summary p {
    padding: 14px 40px 0 40px; text-align: center;
    font-family: "Montserrat", Arial, sans-serif; font-weight: 700;
    font-size: 15px; line-height: 22px;
  }
  .summary p span { display: block; text-align: left; padding-left: 30px; text-align: left; }

  .image-slot {
    position: absolute; background: #fff;
    border: 1.5px solid var(--muted-line);
  }
  .slot-one { left: 884px; top: 410px; width: 110px; height: 112px; transform: rotate(-2deg); }
  .slot-two { left: 752px; top: 482px; width: 114px; height: 116px; transform: rotate(-9deg); }
  .slot-three { left: 1002px; top: 476px; width: 108px; height: 120px; transform: rotate(10deg); }

  .client-logo-slot {
    position: absolute; left: 720px; top: 656px; width: 150px; height: 128px;
    border: 1.5px solid #999; display: flex; align-items: center; justify-content: center;
    font-size: 15px; font-weight: 600;
  }
  .maker-mark {
    position: absolute; left: 922px; top: 718px;
    display: flex; align-items: center; gap: 8px;
  }
  .maker-square { width: 16px; height: 22px; background: var(--accent); }
  .maker-text { font-family: "Montserrat", Arial, sans-serif; line-height: 1; }
  .maker-credit { font-size: 8.5px; letter-spacing: 1px; font-weight: 500; color: #444; }
  .maker-name { font-size: 13px; font-weight: 700; letter-spacing: 2px; margin-top: 3px; }
</style>
</head>
<body>
<main class="profile-card">
  <div class="card-frame"></div>

  <h2 class="section-title motivations-title">What motivates me?</h2>
  <section class="panel motivations">
    <ul class="trait-list">
      <li>Friendship/relationship</li>
      <li>Making me most of every moment</li>
      <li>Value for money</li>
      <li>Well organised</li>
      <li>Fun environment</li>
    </ul>
  </section>

  <h1 class="persona-name">SALLY SOCIAL</h1>

  <section class="panel portrait-panel"></section>
  <div class="photo-frame">
    <div class="photo-placeholder" role="img" aria-label="Portrait photo of the profiled person"></div>
  </div>
  <div class="paper-clip" role="img" aria-label="Paper clip holding the photo"></div>
  <p class="persona-goal">GOAL:<br>Have fun being physically active with like minded people.</p>

  <h2 class="section-title summary-title">Summary/overview</h2>
  <section class="panel summary">
    <p>Summary or overview write in <span>here.</span></p>
  </section>

  <h2 class="section-title behaviour-title">Behaviour</h2>
  <section class="panel behaviour">
    <ul class="trait-list">
      <li>Busy</li>
      <li>No flashy technology</li>
    </ul>
  </section>

  <div class="image-slot slot-one" role="img" aria-label="Image placeholder complementing the profile"></div>
  <div class="image-slot slot-two" role="img" aria-label="Image placeholder complementing the profile"></div>
  <div class="image-slot slot-three" role="img" aria-label="Image placeholder complementing the profile"></div>

  <h2 class="section-title frustrations-title">Frustration/fear/...</h2>
  <section class="panel frustrations">
    <ul class="trait-list">
      <li>Doesn't like down time</li>
      <li>Too competitive</li>
      <li>Wasting my time</li>
      <li>Who's looking after the kids</li>
      <li>I won't be able to play?</li>
    </ul>
  </section>

  <h2 class="section-title pain-title">Pain points</h2>
  <section class="panel pain-points">
    <ul class="trait-list">
      <li>Things must just worth - functional</li>
      <li>You won't be good enough</li>
      <li>Scared of being hurt</li>
      <li>No hit</li>
      <li>Knowledge of rules</li>
    </ul>
  </section>

  <div class="client-logo-slot">Client's logo</div>

  <div class="maker-mark">
    <div class="maker-square"></div>
    <div class="maker-text">
      <div class="maker-credit">DESIGNED AND POWERED BY</div>
      <div class="maker-name">BRIGHT HARBOUR</div>
    </div>
  </div>
</main>
</body>
</html>
```